Walk Beside The River

Business Card design

Target Market(s)

People who require support in the commnity

Industry/Entity Type

Mental Health Support

Contact Information for Business Card

Mental Health Support Rosalind Tavener walkbesidetheriver@mailbrook.com.au 0458 906 312 PO Box 627 Kestrel Vale NSW 2999

Colors
6B429C
8869AF
B7A5CE
E3DAEB
F3F0F8

Requirements
Must have
• Logo & details listed above
Should not have
• No red or orange

```html
<!DOCTYPE html>
<html lang="en">
<head>
<meta charset="utf-8">
<title>Walk Beside The River – Business Card</title>
<link href="https://fonts.googleapis.com/css2?family=Montserrat:wght@500;800&display=swap" rel="stylesheet">
<style>
  :root {
    --purple: #6B429C;
    --purple-soft: #8869AF;
    --lilac: #B7A5CE;
    --sun: #F2EC2C;
    --ink: #1A1A1A;
    --paper: #FFFFFF;
    --backdrop: #3A3A3A;
  }
  * { margin: 0; padding: 0; box-sizing: border-box; }
  html, body { width: 1200px; height: 689px; overflow: hidden; }
  body {
    background: var(--backdrop);
    font-family: "Montserrat", sans-serif;
    position: relative;
  }
  .card {
    position: absolute;
    top: 190px;
    width: 540px;
    height: 309px;
    background: var(--paper);
    border-radius: 16px;
    overflow: hidden;
  }
  .card--front { left: 40px; }
  .card--back { left: 620px; }

  .brand {
    display: flex;
    align-items: center;
    gap: 14px;
    color: var(--purple);
    font-weight: 800;
    text-transform: uppercase;
  }
  .brand__dot {
    border-radius: 50%;
    background: var(--purple);
    flex: none;
  }
  .card--front .brand {
    position: absolute;
    left: 50%; top: 50%;
    transform: translate(-50%, -50%);
    font-size: 22px;
    white-space: nowrap;
  }
  .card--front .brand__dot { width: 46px; height: 46px; }

  .card--back .brand {
    position: absolute;
    left: 150px; top: 38px;
    font-size: 15px;
    gap: 10px;
    white-space: nowrap;
  }
  .card--back .brand__dot { width: 34px; height: 34px; }

  .back__swoosh { position: absolute; inset: 0; }

  .details {
    position: absolute;
    left: 92px; top: 108px;
    color: var(--ink);
  }
  .details__title {
    color: var(--purple);
    font-weight: 800;
    font-size: 13.5px;
    letter-spacing: 0.2px;
    text-transform: uppercase;
    margin-bottom: 8px;
    white-space: nowrap;
  }
  .details__row {
    display: flex;
    align-items: center;
    gap: 6px;
    font-weight: 500;
    font-size: 12.5px;
    margin-bottom: 6px;
    white-space: nowrap;
  }
  .details__row--indent { padding-left: 26px; }
  .details__item { display: inline-flex; align-items: center; gap: 5px; margin-right: 6px; }
  .icon { width: 13px; height: 13px; fill: var(--purple); flex: none; }
</style>
</head>
<body>

  <section class="card card--front">
    <div class="brand">
      <span class="brand__dot"></span>
      <span class="brand__name">Walk Beside The River</span>
    </div>
  </section>

  <section class="card card--back">
    <svg class="back__swoosh" viewBox="0 0 540 309" width="540" height="309" aria-hidden="true">
      <path d="M0,282 Q360,290 540,172 L540,309 L0,309 Z" fill="var(--purple)"/>
      <path d="M70,268 Q380,246 522,148" fill="none" stroke="var(--sun)" stroke-width="4" stroke-linecap="round"/>
    </svg>

    <div class="brand">
      <span class="brand__dot"></span>
      <span class="brand__name">Walk Beside The River</span>
    </div>

    <div class="details">
      <p class="details__title">Mental Health Support Rosalind Tavener</p>
      <p class="details__row details__row--indent">
        <svg class="icon" viewBox="0 0 24 24" aria-hidden="true"><path d="M12 2a7 7 0 0 0-7 7c0 5 7 13 7 13s7-8 7-13a7 7 0 0 0-7-7zm0 9.5A2.5 2.5 0 1 1 12 6.5a2.5 2.5 0 0 1 0 5z"/></svg>
        PO Box 627 Kestrel Vale NSW 2999
      </p>
      <p class="details__row">
        <span class="details__item">
          <svg class="icon" viewBox="0 0 24 24" aria-hidden="true"><path d="M6.6 10.8a15.1 15.1 0 0 0 6.6 6.6l2.2-2.2a1 1 0 0 1 1-.25 11.4 11.4 0 0 0 3.6.57 1 1 0 0 1 1 1V20a1 1 0 0 1-1 1A17 17 0 0 1 3 4a1 1 0 0 1 1-1h3.5a1 1 0 0 1 1 1c0 1.25.2 2.45.57 3.6a1 1 0 0 1-.25 1z"/></svg>
          0458 906 312
        </span>
        <span class="details__item">
          <svg class="icon" viewBox="0 0 24 24" aria-hidden="true"><rect x="2" y="5" width="20" height="14" rx="1.5"/><path d="M3 6.5l9 6.5 9-6.5" fill="none" stroke="#fff" stroke-width="1.8"/></svg>
          walkbesidetheriver@mailbrook.com.au
        </span>
      </p>
    </div>
  </section>

</body>
</html>
```